Business Card

Just need business logo with phone number on it. 0487 312 556
And the following on the bottom of the card.

"Your local plumbing experts".
and emblems for kelpa card, cheque and cash

```html
<!DOCTYPE html>
<html lang="en">
<head>
<meta charset="utf-8">
<title>Eastvale Plumbing &amp; Drainage – Business Card</title>
<link rel="stylesheet" href="https://fonts.googleapis.com/css2?family=Roboto:wght@500;700&display=swap">
<style>
  :root {
    --backdrop: #232323;
    --card-white: #ffffff;
    --brand-red: #ea202c;
    --brand-blue: #1a8fd0;
    --ink-grey: #555555;
    --ink-black: #111111;
  }
  html, body {
    margin: 0;
    padding: 0;
    width: 1200px;
    height: 900px;
    overflow: hidden;
    background: var(--backdrop);
    font-family: "Roboto", Arial, sans-serif;
  }
  .stage { position: relative; width: 1200px; height: 900px; }
  .card {
    position: absolute;
    box-shadow: 3px 4px 8px rgba(0,0,0,0.55);
    overflow: hidden;
  }
  .card-front { left: 319px; top: 87px; width: 581px; height: 358px; background: var(--card-white); }
  .card-back  { left: 319px; top: 477px; width: 584px; height: 360px; background: var(--brand-red); }

  .brand-name {
    position: absolute;
    right: 32px;
    top: 34px;
    text-align: right;
    color: var(--brand-red);
    font-weight: 700;
    line-height: 1;
    margin: 0;
  }
  .brand-name .brand-initials { display: block; font-size: 46px; letter-spacing: 1px; }
  .brand-name .brand-title { display: block; font-size: 29px; letter-spacing: 1px; margin-top: 8px; }
  .brand-name .brand-trade { display: block; font-size: 16px; letter-spacing: 3px; margin-top: 4px; }

  .phone {
    position: absolute;
    left: 46px;
    top: 236px;
    display: flex;
    align-items: center;
    gap: 8px;
    font-size: 28px;
    font-weight: 500;
    color: var(--ink-grey);
    letter-spacing: 0.5px;
  }
  .phone svg { width: 26px; height: 26px; }

  .tagline-band {
    position: absolute;
    left: 0;
    top: 284px;
    width: 363px;
    height: 40px;
    background: var(--brand-red);
    color: #fff;
    font-size: 18px;
    font-weight: 500;
    line-height: 40px;
    padding-left: 41px;
    box-sizing: border-box;
    letter-spacing: 0.2px;
  }
  .tagline-rule {
    position: absolute;
    left: 0;
    top: 328px;
    width: 363px;
    height: 5px;
    background: var(--brand-blue);
  }

  .payment-methods { position: absolute; left: 376px; top: 290px; display: flex; gap: 10px; }
  .pay-card {
    width: 43px; height: 30px; box-sizing: border-box;
    border: 2px solid var(--ink-black); border-radius: 4px;
    font-size: 12px; font-weight: 700; color: var(--ink-black);
    display: flex; align-items: center; justify-content: center;
  }
  .pay-cheque svg { width: 62px; height: 30px; display: block; }
  .pay-cash svg { width: 47px; height: 30px; display: block; }

  .back-name {
    position: absolute;
    left: 0; right: 0;
    top: 156px;
    text-align: center;
    color: #fff;
    font-size: 54px;
    font-weight: 700;
    letter-spacing: 1px;
    line-height: 1;
    margin: 0;
  }
  .back-band {
    position: absolute;
    left: 0; bottom: 0;
    width: 100%; height: 24px;
    background: var(--brand-blue);
  }
</style>
</head>
<body>
<main class="stage">
  <section class="card card-front">
    <h1 class="brand-name">
      <span class="brand-initials">EVPD</span>
      <span class="brand-title">EASTVALE</span>
      <span class="brand-trade">PLUMBING &amp; DRAINAGE</span>
    </h1>

    <div class="phone">
      <svg viewBox="0 0 26 26" aria-hidden="true">
        <circle cx="13" cy="13" r="11.5" fill="none" stroke="var(--brand-blue)" stroke-width="2"/>
        <path d="M9.2 7.5c.6-.5 1.3-.4 1.7.2l1.1 1.7c.3.5.2 1.1-.2 1.5l-.7.6c.6 1.5 1.7 2.7 3.2 3.4l.6-.7c.4-.4 1-.5 1.5-.2l1.7 1.1c.6.4.7 1.2.2 1.7l-.8.9c-.6.6-1.5.8-2.3.5-3.2-1.2-5.6-3.7-6.8-6.9-.3-.8-.1-1.7.5-2.3z" fill="var(--brand-red)"/>
      </svg>
      <span>0487 312 556</span>
    </div>

    <div class="tagline-band">YOUR LOCAL PLUMBING EXPERTS</div>
    <div class="tagline-rule"></div>

    <div class="payment-methods">
      <div class="pay-card">kelpa</div>
      <div class="pay-cheque">
        <svg viewBox="0 0 62 30" aria-label="Cheque">
          <rect x="1" y="1" width="60" height="28" rx="2" fill="#fff" stroke="var(--ink-black)" stroke-width="2"/>
          <rect x="5" y="5" width="52" height="20" fill="none" stroke="var(--ink-black)" stroke-width="1"/>
          <line x1="9" y1="11" x2="40" y2="11" stroke="var(--ink-black)" stroke-width="1"/>
          <line x1="9" y1="15" x2="52" y2="15" stroke="var(--ink-black)" stroke-width="1"/>
          <rect x="9" y="19" width="16" height="3" fill="var(--ink-black)"/>
          <line x1="34" y1="21" x2="52" y2="21" stroke="var(--ink-black)" stroke-width="1"/>
        </svg>
      </div>
      <div class="pay-cash">
        <svg viewBox="0 0 47 30" aria-label="Cash">
          <rect x="0" y="0" width="47" height="30" rx="2" fill="var(--ink-black)"/>
          <circle cx="23.5" cy="15" r="7.5" fill="#fff"/>
          <text x="23.5" y="19" text-anchor="middle" font-family="Roboto, Arial, sans-serif" font-weight="700" font-size="11" fill="var(--ink-black)">$</text>
        </svg>
      </div>
    </div>
  </section>

  <section class="card card-back">
    <p class="back-name">EVPD</p>
    <div class="back-band"></div>
  </section>
</main>
</body>
</html>
```